Toravex Systems Brochure

I am looking for a brochure layout, either a tri fold or double fold which ever fits the design better. I have listed a little info below concerning the services Toravex Tech provides.

The name of my company is Toravex Systems, that offers a wide range of services. Services that we offer are (Fiber optic solutions, Audio visual services, voice and date infrastructure, wireless capabilities, and sound system design). We have done work for a wide range of clients ranges from small offices to major retail stores. I would like to create a brochure that helps market my company. Something to hand to my customers on the job therefore they will have a great idea of all the services that we offer. I really like the idea of a roadmap, for example if there was a picture of an office area we could have an arrow pointing to the conference room and say audio visual solutions and give a little blurb about what that exactly means. (short and concise). To help describe some of our services you can look at our website to get a better idea of what exactly it is that we offer. http://www.toravexsys-example.com/ Look forward to hearing back from you and seeing what you can come up with for us!
Updates

Target Market(s)

current and future clients, interested in upgrading their current technology infrastructure.

Colors

Designer to choose colors to be used in the design.

Requirements
Must have
• Services offered
• Brief explanation of services offered
• Contact information
Nice to have
• Why choose Toravex section.

```html
<!DOCTYPE html>
<html lang="en">
<head>
<meta charset="utf-8">
<title>Toravex Systems Brochure</title>
<link rel="stylesheet" href="https://fonts.googleapis.com/css2?family=Saira+Condensed:wght@400;500;600;700&family=Roboto:wght@700&display=swap">
<style>
:root{
  --blue:#3f5ea8;
  --blue-dark:#2f4a8c;
  --green:#6aae6e;
  --green-light:#8cc48f;
  --navy:#0a1733;
  --teal:#7fb6cc;
  --ink:#2b2b2b;
  --grey:#e3e6ea;
  --page:#ffffff;
  --bg:#ececec;
}
*{margin:0;padding:0;box-sizing:border-box}
html,body{width:1200px;height:1000px;overflow:hidden;background:var(--bg)}
body{position:relative;font-family:"Saira Condensed",sans-serif;color:var(--ink)}
.sheet{position:absolute;left:297px;width:606px;height:467px;background:var(--page);overflow:hidden}
.sheet--outside{top:18px}
.sheet--inside{top:507px;height:466px}
.abs{position:absolute}
.photo{position:absolute;border:3px solid var(--green);border-radius:22px;overflow:hidden}
.photo svg{display:block;width:100%;height:100%}

/* outside: about panel */
.about-title{left:6px;top:14px;font-size:14px;font-weight:700;color:var(--blue);letter-spacing:.3px}
.about-rule{left:6px;top:30px;width:180px;height:3px;background:linear-gradient(90deg,var(--blue),var(--green))}
.about-text{left:6px;top:40px;width:188px;font-size:7.4px;line-height:9px;text-align:justify}
.why-title{left:0;width:203px;top:125px;text-align:center;font-size:16px;font-weight:600;color:var(--blue)}
.why-num{left:22px;font-size:38px;font-weight:600;color:var(--blue);opacity:.55;line-height:1}
.why-box{left:43px;width:117px;color:#fff;text-align:center;padding-top:3px}
.why-box h3{font-family:"Roboto",sans-serif;font-size:11.5px;letter-spacing:.3px}
.why-box p{font-size:8px;line-height:9.5px}
.why-box--blue{background:var(--blue)}
.why-box--green{background:var(--green)}
.closing-text{left:6px;top:399px;width:190px;font-size:7.4px;line-height:9px;text-align:justify}

/* outside: cover */
.cover-title{left:414px;top:22px;font-size:18px;line-height:22px;font-weight:500;color:var(--teal);letter-spacing:.3px}
.cover-title b{color:#a8d6e6;font-weight:600}
.brand{font-weight:500;color:var(--blue-dark);white-space:nowrap}
.brand--back{left:256px;top:379px;font-size:14px}
.brand--front{left:418px;top:430px;font-size:17px}
.contact{font-size:7.5px;color:var(--ink)}
.contact-address{left:240px;top:413px}
.contact-row{left:240px;width:180px;display:flex}
.contact-row span{flex:1}
.contact-row span+span{border-left:1px solid #555;padding-left:3px}

/* inside */
.bg-left{left:0;top:0;width:203px;height:466px;background:var(--green-light)}
.bg-mid{left:203px;top:0;width:203px;height:466px;background:var(--grey)}
.bg-right{left:406px;top:0;width:200px;height:466px;background:var(--blue)}
.sec-head{display:flex;align-items:center;gap:6px;font-family:"Roboto",sans-serif;font-size:11.5px;line-height:11px;letter-spacing:.3px}
.sec-head--blue{color:var(--blue-dark)}
.sec-head--white{color:#fff}
.sec-text{font-size:8px;line-height:9px}
.sec-text--white{color:#fff}
.cols{display:flex;gap:6px}
.cols ul{list-style:none}
.list{list-style:none}
</style>
</head>
<body>

<!-- OUTSIDE SPREAD -->
<section class="sheet sheet--outside">
  <svg class="abs" style="left:0;top:0" width="203" height="467" role="img" aria-label="Faded photo of network cables behind the why choose us list">
    <defs><linearGradient id="fade" x1="0" y1="0" x2="1" y2="1"><stop offset="0" stop-color="#ffffff"/><stop offset=".5" stop-color="#e6e8ec"/><stop offset="1" stop-color="#ffffff"/></linearGradient></defs>
    <rect x="0" y="120" width="203" height="280" fill="url(#fade)"/>
  </svg>

  <h2 class="abs about-title">ABOUT US</h2>
  <div class="abs about-rule"></div>
  <p class="abs about-text">Toravex Systems has been an innovator in installing, voice, data, audio/ video and fiber optic systems. Delivering powerful one-stop solutions to small, medium and large businesses, hospitals, schools and universities throughout the United States. Keeping current with continuing changes in voice and data network technologies, audio/ video requirements, cabling standards and new communication products has made Toravex Systems the obvious choice for organizations that want to optimize their IT investment.</p>

  <h2 class="abs why-title">WHY CHOOSE US</h2>
  <span class="abs why-num" style="top:170px">1</span>
  <span class="abs why-num" style="top:218px">2</span>
  <span class="abs why-num" style="top:268px">3</span>
  <span class="abs why-num" style="top:318px">4</span>
  <span class="abs why-num" style="top:350px">5</span>
  <div class="abs why-box why-box--blue" style="top:145px;height:50px"><h3>FLEXIBLE</h3><p>Flexible enough to handle singe site and large multi-site business installations.</p></div>
  <div class="abs why-box why-box--green" style="top:195px;height:48px"><h3>DEPENDABLE</h3><p>Highly trained technicians nsure that each install is done professionally.</p></div>
  <div class="abs why-box why-box--blue" style="top:243px;height:50px"><h3>SCALABLE</h3><p>Experienced project managers provide guidance to enable business to expand.</p></div>
  <div class="abs why-box why-box--green" style="top:293px;height:50px;padding-top:9px"><h3>RELIABLE</h3><p>Provide "End to End" solutions to all business.</p></div>
  <div class="abs why-box why-box--blue" style="top:343px;height:47px;padding-top:10px"><h3>COVERAGE</h3><p>Nationwide.</p></div>

  <p class="abs closing-text">Superior workmanship, turnkey solutions backed by fast turnaround and professional service is what makes Toravex Systems the ideal business partner for your organization. Evaluating your needs, designing a solution and selecting the best products to meet your requirements is part of Toravex Systems total business support package.</p>

  <svg class="abs" style="left:203px;top:0" width="403" height="467" viewBox="203 0 403 467">
    <defs>
      <radialGradient id="space" cx=".6" cy=".55" r=".7">
        <stop offset="0" stop-color="#4a7fc7"/><stop offset=".45" stop-color="#1a3d78"/><stop offset="1" stop-color="#070f24"/>
      </radialGradient>
    </defs>
    <rect x="203" y="0" width="403" height="420" fill="url(#space)" role="img" aria-label="Photo of the earth from space wrapped in glowing network lines"/>
    <path d="M203 372 C235 330 275 310 330 318 C420 330 500 385 606 392 L606 467 L203 467 Z" fill="var(--blue)"/>
    <path d="M203 376 C235 336 275 317 330 324 C420 336 500 391 606 398 L606 467 L203 467 Z" fill="var(--green)"/>
    <path d="M203 380 C235 342 275 323 330 330 C420 342 500 397 606 404 L606 467 L203 467 Z" fill="#fff"/>
  </svg>
  <div class="photo" style="left:240px;top:20px;width:110px;height:100px" role="img" aria-label="Photo of hands reviewing charts on paper"><svg><rect width="100%" height="100%" fill="#c9d3e0"/></svg></div>
  <div class="photo" style="left:313px;top:103px;width:76px;height:76px" role="img" aria-label="Photo of a server rack with binary digits"><svg><rect width="100%" height="100%" fill="#2a3340"/></svg></div>
  <div class="photo" style="left:215px;top:152px;width:92px;height:90px" role="img" aria-label="Photo of patch cables in a network switch"><svg><rect width="100%" height="100%" fill="#8a9bb0"/></svg></div>

  <h1 class="abs cover-title">YOUR <b>IT</b> CONNECTION<br>TO THE FUTURE</h1>

  <div class="abs brand brand--back">Toravex Systems</div>
  <div class="abs contact contact-address">14-B Halden Road, Brookvale, MA 01899</div>
  <div class="abs contact contact-row" style="top:434px"><span>T:&nbsp; 555-201-0921</span><span>F:&nbsp; 555-201-0918</span></div>
  <div class="abs contact contact-row" style="top:444px"><span>info@toravexsys-example.com</span><span>www.toravexsys-example.com</span></div>
  <div class="abs brand brand--front">Toravex Systems</div>
</section>

<!-- INSIDE SPREAD -->
<section class="sheet sheet--inside">
  <div class="abs bg-left"></div>
  <div class="abs bg-mid"></div>
  <div class="abs bg-right"></div>
  <svg class="abs" style="left:0;top:0" width="606" height="466">
    <polygon points="0,320 203,300 203,466 0,466" fill="var(--blue)"/>
    <polygon points="406,330 606,290 606,466 406,466" fill="var(--green)"/>
    <polygon points="150,240 300,150 470,240 470,466 150,466" fill="#b9d3e6" role="img" aria-label="Isometric illustration of an office floor with conference room, desks and a support agent"/>
  </svg>

  <div class="abs" style="left:10px;top:16px;width:190px">
    <h2 class="sec-head sec-head--blue"><svg width="12" height="12"><polygon points="1,0 12,6 1,12" fill="var(--blue)"/></svg>AUDIO VISUAL SERVICES</h2>
    <p class="sec-text" style="margin-top:8px">Toravex Systems provide a full spectrum of products and services to meet your specific communications needs:</p>
    <div class="cols sec-text">
      <ul><li>- Nationwide Telephone</li><li>- System Installation</li><li>- Telephone System</li><li>&nbsp; Maintenance</li><li>- VOIP Systems</li></ul>
      <ul><li>- Digital Telephone</li><li>&nbsp; Systems</li><li>- Voicemail</li></ul>
    </div>
  </div>
  <div class="photo" style="left:37px;top:117px;width:110px;height:100px" role="img" aria-label="Photo of a team in a video conference room"><svg><rect width="100%" height="100%" fill="#cfd6de"/></svg></div>
  <div class="photo" style="left:30px;top:230px;width:105px;height:95px" role="img" aria-label="Photo of glowing blue fiber optic strands"><svg><rect width="100%" height="100%" fill="#1f4f86"/></svg></div>

  <div class="abs" style="left:10px;top:334px;width:190px">
    <h2 class="sec-head sec-head--white"><svg width="20" height="10"><line x1="0" y1="5" x2="16" y2="5" stroke="#fff" stroke-width="1.5"/><circle cx="3" cy="5" r="2.5" fill="#fff"/><rect x="15" y="2" width="5" height="6" fill="#fff"/></svg>FIBER OPTIC<br>SOLUTIONS</h2>
    <p class="sec-text sec-text--white" style="margin-top:6px">Our Nationwide Professionally Trained Technicians And Experienced Project Management Team Provide:</p>
    <div class="cols sec-text sec-text--white">
      <ul><li>- Site Surveys</li><li>- Network Design / Build</li><li>- Voice &amp; Data Cabling</li><li>- LAN / WAN Cabling</li><li>- Fiber Optic Cabling</li><li>- Outside Plant Cabling</li></ul>
      <ul><li>- Data Center Design</li><li>&nbsp; and Installation</li><li>- Surveillance Systems</li><li>- Telephone Systems</li><li>- Audio / Video Cabling</li><li>- POS Systems</li></ul>
    </div>
  </div>

  <div class="abs" style="left:212px;top:16px;width:185px">
    <h2 class="sec-head sec-head--blue"><svg width="14" height="14"><rect x="0" y="8" width="3" height="6" fill="var(--blue)"/><rect x="5" y="5" width="3" height="9" fill="var(--blue)"/><rect x="10" y="1" width="3" height="13" fill="var(--blue)"/></svg>SOUND SYSTEM DESIGN</h2>
    <p class="sec-text" style="margin-top:6px;color:#555">You can working one on one with a qualified technician to create a one of a kind system that perfectly meets your companies needs.</p>
  </div>
  <div class="photo" style="left:298px;top:62px;width:64px;height:60px;border-color:#999" role="img" aria-label="Photo of a studio microphone"><svg><rect width="100%" height="100%" fill="#c8a878"/></svg></div>

  <div class="abs" style="left:416px;top:16px;width:185px">
    <h2 class="sec-head sec-head--white">WIRELESS CAPABILITIES <svg width="18" height="14"><path d="M2 6 Q9 -1 16 6" stroke="#fff" stroke-width="2" fill="none"/><path d="M5 9 Q9 5 13 9" stroke="#fff" stroke-width="2" fill="none"/><circle cx="9" cy="12" r="1.6" fill="#fff"/></svg></h2>
    <p class="sec-text sec-text--white" style="margin-top:8px">Toravex's Wireless Services Include:</p>
    <ul class="list sec-text sec-text--white"><li>- Site Survey</li><li>- LAN Design and Installation</li><li>- Access Point &amp; Antenna Installation and</li><li>&nbsp; configuration</li><li>- Client Devises and Print Servers</li><li>- VOIP Systems</li><li>- Surveillance Cameras</li><li>- Speakers</li></ul>
  </div>
  <div class="photo" style="left:478px;top:125px;width:102px;height:92px" role="img" aria-label="Photo of a ceiling surveillance camera"><svg><rect width="100%" height="100%" fill="#d8dde3"/></svg></div>
  <div class="photo" style="left:520px;top:213px;width:72px;height:70px" role="img" aria-label="Photo of a hand on a tablet"><svg><rect width="100%" height="100%" fill="#9aa8b6"/></svg></div>
  <div class="photo" style="left:452px;top:262px;width:80px;height:80px;border-color:#fff" role="img" aria-label="Photo of a data center aisle"><svg><rect width="100%" height="100%" fill="#c2c9d2"/></svg></div>

  <div class="abs" style="left:416px;top:340px;width:185px">
    <h2 class="sec-head sec-head--blue" style="justify-content:flex-end;text-align:right">VOICE &amp; DATA<br>INFRASTRUCTURE <svg width="10" height="16"><rect x="2" y="0" width="6" height="10" rx="3" fill="var(--blue)"/><path d="M0 8 Q5 15 10 8" stroke="var(--blue)" fill="none" stroke-width="1.4"/><line x1="5" y1="12" x2="5" y2="16" stroke="var(--blue)" stroke-width="1.4"/></svg></h2>
    <p class="sec-text sec-text--white" style="margin-top:4px">We partner with some of the top manufactures in the industry to offer minimum downtime, maximize reliability and reduce cost of ownership.</p>
    <ul class="list sec-text sec-text--white"><li>- 10 &amp; 40 gigabit Copper and Fiber Solutions</li><li>- Structured Cabling</li><li>- Cabinets, Racks and Ladder Tray, Fiber runner</li><li>- Under Floor Solutions</li><li>- Pre-Terminated Copper &amp; Fiber Solutions</li><li>- Clean Up and De-Installation</li><li>- Moves, Adds and Changes</li></ul>
  </div>
</section>

</body>
</html>
```